Holistic/ Sports Psychologist needs flyer design

I need a flyer designed that catches the attention of potential customers - (parents of young athletes and athletes) who may be looking for psychological services. I have a logo and all the relevant info for the flyer but would like someone to take it and make it look creative, fun, fresh and attention getting for high school and college athletes. The colors used can be from my logo design which represents my holistic approach.
Target Market(s)
high school and collegiate athletes
Industry/Entity Type
sports psychology
Requirements
Must have
- Info I put on the flyer with my logo and please add some graphics and color based on my logo

```html
<!DOCTYPE html>
<html lang="en">
<head>
<meta charset="utf-8">
<title>Holistic Psychology Flyer</title>
<link rel="stylesheet" href="https://fonts.googleapis.com/css2?family=Baloo+2:wght@700;800&family=Poppins:ital,wght@0,400;0,500;0,600;0,700;1,400;1,600;1,700&display=swap">
<style>
  :root {
    --navy: #274a7d;
    --blue: #2c5795;
    --green: #92c352;
    --green-soft: #c9e3a8;
    --panel: #e6f0f8;
    --ink: #2b2f36;
    --page: #d4d5d8;
    --white: #ffffff;
  }
  * { margin: 0; padding: 0; box-sizing: border-box; }
  html, body { width: 1200px; height: 800px; overflow: hidden; }
  body {
    background: var(--page);
    font-family: "Poppins", sans-serif;
    color: var(--ink);
    display: flex; align-items: center; justify-content: center;
  }
  .flyer {
    position: relative;
    width: 600px; height: 776px;
    background: var(--white);
    overflow: hidden;
    box-shadow: 0 6px 24px rgba(0,0,0,.18);
  }
  .corner-blobs { position: absolute; top: 0; right: 0; }

  /* Header */
  .brand {
    position: absolute; top: 26px; left: 40px;
    display: flex; align-items: center; gap: 14px;
  }
  .brand-mark { width: 66px; height: 66px; border-radius: 50%; background: var(--blue); }
  .brand-name { font-size: 24px; font-weight: 500; color: var(--blue); letter-spacing: .5px; }
  .brand-bar {
    position: absolute; top: 90px; left: 110px;
    width: 300px; height: 16px; background: var(--green);
  }
  .headline {
    position: absolute; top: 132px; left: 40px;
    font-family: "Baloo 2", sans-serif; font-weight: 800;
    color: var(--blue); line-height: .9; font-size: 48px;
  }
  .subhead {
    position: absolute; top: 224px; left: 40px;
    font-family: "Baloo 2", sans-serif; font-weight: 700;
    color: var(--blue); font-size: 20px;
  }
  .telehealth {
    position: absolute; top: 134px; right: 40px;
    display: flex; align-items: center; gap: 10px;
  }
  .telehealth-lead { font-size: 12px; line-height: 1.1; }
  .telehealth-word {
    font-family: "Baloo 2", sans-serif; font-weight: 800;
    font-size: 34px; line-height: .9; color: var(--ink);
  }
  .sessions {
    position: absolute; top: 200px; right: 40px;
    display: flex; align-items: center; gap: 8px; text-align: right;
    font-size: 11px; line-height: 1.2;
  }
  .sessions strong { font-weight: 700; font-size: 13px; }

  /* Content panel */
  .panel {
    position: absolute; top: 262px; left: 0; width: 100%; bottom: 0;
    background: linear-gradient(180deg, #eef4fa 0%, var(--panel) 100%);
    padding: 16px 40px 0;
    display: flex; flex-direction: column; gap: 10px;
  }
  .ways-title { font-weight: 700; font-size: 16px; line-height: 1.25; color: var(--ink); }
  .services { list-style: none; font-size: 9.5px; line-height: 1.3; }
  .services li { margin-bottom: 5px; padding-left: 14px; position: relative; }
  .services li::before {
    content: ""; position: absolute; left: 0; top: 4px;
    width: 8px; height: 3px; background: var(--blue); transform: skewX(-30deg) rotate(-30deg);
  }
  .services b { display: block; font-weight: 700; text-transform: uppercase; }
  .services span { display: block; font-style: italic; }
  .background-tag { display: flex; align-items: center; }
  .background-tag::before { content: ""; width: 16px; height: 26px; background: var(--green); }
  .background-tag h2 {
    background: var(--blue); color: var(--white);
    font-weight: 600; font-style: italic; font-size: 15px; line-height: 26px;
    padding: 0 22px 0 14px;
  }
  .bio { font-size: 9.5px; line-height: 1.35; font-style: italic; }
  .bio p + p { margin-top: 5px; }
  .bio strong { font-weight: 700; }

  /* Footer */
  .footer-wave { position: absolute; left: 0; bottom: 0; }
  .address {
    position: absolute; left: 40px; bottom: 22px;
    color: var(--white); font-weight: 700; font-style: italic;
    font-size: 12px; line-height: 1.3;
  }
  .contact { position: absolute; right: 40px; bottom: 16px; text-align: right; color: var(--white); }
  .contact-web { font-size: 10px; letter-spacing: 2px; }
  .contact-phone {
    display: flex; align-items: center; gap: 8px; justify-content: flex-end;
    font-weight: 700; font-style: italic; font-size: 22px;
  }
</style>
</head>
<body>
<main class="flyer">
  <svg class="corner-blobs" width="200" height="170" viewBox="0 0 200 170" aria-hidden="true">
    <circle cx="70" cy="0" r="75" fill="var(--green-soft)"/>
    <circle cx="200" cy="50" r="100" fill="var(--green-soft)"/>
  </svg>

  <header class="brand">
    <div class="brand-mark"></div>
    <div class="brand-name">Dr. Elena Whitford</div>
  </header>
  <div class="brand-bar"></div>

  <h1 class="headline">Holistic<br>Psychology</h1>
  <p class="subhead">and sports Psychology Consulting</p>

  <div class="telehealth">
    <svg width="56" height="52" viewBox="0 0 62 58" aria-hidden="true">
      <rect x="3" y="3" width="56" height="38" rx="3" fill="none" stroke="var(--ink)" stroke-width="4"/>
      <path d="M24 50h14M31 41v9" stroke="var(--ink)" stroke-width="4"/>
      <path d="M10 22h12l4-8 6 16 4-8h16" fill="none" stroke="var(--ink)" stroke-width="3"/>
    </svg>
    <div>
      <div class="telehealth-lead">All services are provided<br>online via</div>
      <div class="telehealth-word">telehealth</div>
    </div>
  </div>

  <div class="sessions">
    <div>Sessions are<br><strong>30 or 55 minutes</strong></div>
    <svg width="28" height="32" viewBox="0 0 30 34" aria-hidden="true">
      <circle cx="15" cy="19" r="12" fill="none" stroke="var(--ink)" stroke-width="3.5"/>
      <path d="M11 3h8M15 3v4" stroke="var(--ink)" stroke-width="3"/>
      <path d="M15 19V11a8 8 0 0 1 0 16z" fill="var(--ink)"/>
    </svg>
  </div>

  <section class="panel">
    <h2 class="ways-title">Ways to Improve Athletic Performance Using Sports and Holistic Psychology</h2>
    <ul class="services">
      <li><b>Mental Skills Training</b><span>Ex: visualization, goal-setting, motivation, self- talk, mindset, concentration techniques.</span></li>
      <li><b>Performance Enhancement</b><span>Eliminate psychological barriers that are hindering performance such as self- doubt, perfectionism, fear of failure, and burnout.</span></li>
      <li><b>Mental Health</b><span>Anxiety and stress management by using relaxation techniques, breathwork, and mindfulness practices.</span></li>
      <li><b>Injury Recovery Support</b><span>Assist athletes in maintaining resilience and positive mental attitude during rehabilitation as well as processing emotions relating to any potential trauma caused by the injury or life transitions resulting from it.</span></li>
      <li><b>Burnout Prevention</b><span>Teach athletes how to have balance in sports and life so they can experience longevity in their sports as well as overall optimal health and well-being.</span></li>
    </ul>

    <div class="background-tag"><h2>Background</h2></div>
    <div class="bio">
      <p><strong>Dr. Elena Whitford</strong> is a licensed psychologist. She understands the unique experiences of athletes due to her background as an All-American swimmer, collegiate and age group swim coach, parent of a collegiate/professional athlete, and sports psychology researcher. She works with athletes to optimize performance and overall well-being.</p>
      <p>Her specializations include: performance anxiety, mental performance, stress management, anxiety, depressions, trauma, life transitions, relationship issues, injury, and sleep.</p>
    </div>
  </section>

  <svg class="footer-wave" width="600" height="100" viewBox="0 0 600 100" aria-hidden="true">
    <path d="M0 14 Q300 96 600 22 V100 H0z" fill="var(--green)"/>
    <path d="M0 28 Q300 110 600 36 V100 H0z" fill="var(--navy)"/>
  </svg>
  <address class="address">582 Harbor Lane #110<br>Coral Point, FL 32100</address>
  <div class="contact">
    <div class="contact-web">drelenawhitford.com</div>
    <div class="contact-phone">
      <svg width="14" height="18" viewBox="0 0 14 18" aria-hidden="true">
        <rect x="1.5" y="1.5" width="11" height="15" rx="2" fill="none" stroke="var(--green)" stroke-width="2"/>
      </svg>
      555-201-7788
    </div>
  </div>
</main>
</body>
</html>
```